Ember Lane - tailored CVs templates

Wanting 6 -8 C.V templates that are professional and can be used to sent to a human resource manager. The market base is wide so generic is best to cover all areas however a couple of designer templates would be great. The main type of customers requiring CVs are business oriented however there is retail, construction, health and all the key arers of employment.

Target Market(s)

Anyone applying for a job to human resource department

Industry/Entity Type

Business

Colors

Designer to choose colors to be used in the design.

Requirements
Must have
• a good layout, easy to read format, must be able to write details on for cusomters eg work experince etc.
Nice to have
• looking for a range of 6 - 8 differnet templates, majority geneic and couple desiger templates

```html
<!DOCTYPE html>
<html lang="en">
<head>
<meta charset="utf-8">
<title>Ember Lane – CV Template</title>
<link rel="stylesheet" href="https://fonts.googleapis.com/css2?family=Open+Sans:wght@400;600;700&display=swap">
<style>
  :root {
    --bg: #e9eaec;
    --paper: #ffffff;
    --side: #eeeff0;
    --blue: #2f6aa8;
    --blue-dark: #1f4f82;
    --ink: #3d4246;
    --muted: #8a8f94;
    --rule: #d6d8db;
    --bar-grey: #c5c8cc;
  }
  * { box-sizing: border-box; margin: 0; padding: 0; }
  html, body { width: 1200px; height: 799px; overflow: hidden; }
  body { background: var(--bg); font-family: "Open Sans", Arial, sans-serif; color: var(--ink); position: relative; }

  .cv { position: absolute; left: 330px; top: 18px; width: 540px; height: 764px; background: var(--paper); box-shadow: 0 3px 14px rgba(0,0,0,.12); overflow: hidden; }
  .sidebar { position: absolute; left: 0; top: 150px; width: 172px; bottom: 0; background: var(--side); }
  .abs { position: absolute; }

  .name { left: 192px; top: 50px; font-size: 24px; font-weight: 700; color: var(--blue); letter-spacing: -.3px; }
  .job-title { left: 194px; top: 82px; font-size: 7px; letter-spacing: 2px; color: var(--muted); text-transform: uppercase; }

  .contact { right: 24px; top: 22px; text-align: right; font-size: 6.5px; line-height: 11px; color: var(--ink); }
  .contact li { list-style: none; display: flex; justify-content: flex-end; align-items: center; gap: 6px; }
  .contact .ico { width: 7px; height: 7px; background: var(--blue); display: inline-block; }

  .rings { left: 192px; top: 100px; display: flex; gap: 22px; }
  .ring { width: 60px; text-align: center; }
  .ring svg { display: block; margin: 0 auto; }
  .ring .lbl { font-size: 5.5px; color: var(--muted); line-height: 7px; margin-top: 3px; }

  .photo { left: 34px; top: 120px; width: 104px; height: 104px; border-radius: 50%; border: 5px solid #fff; box-shadow: 0 0 0 1px var(--rule); background: radial-gradient(circle at 50% 40%, #b8b2aa 0%, #6d6a66 55%, #3d3b3a 100%); }

  .side-head { font-size: 9px; font-weight: 700; letter-spacing: 2.5px; color: var(--blue); text-transform: uppercase; }
  .side-text { font-size: 6px; line-height: 9px; color: var(--muted); }
  .side-text b { color: var(--blue); font-weight: 600; display: block; }

  .para { font-size: 6.3px; line-height: 9.5px; color: var(--muted); }
  .rule { height: 1px; background: var(--rule); }

  .entry { left: 200px; width: 310px; }
  .entry h4 { font-size: 7px; color: var(--blue); font-weight: 700; position: relative; margin-bottom: 2px; }
  .entry h4::before { content: ""; position: absolute; left: -9px; top: 2px; width: 5px; height: 5px; background: var(--blue); }

  .col-head { font-size: 9px; font-weight: 700; letter-spacing: 2.5px; color: var(--blue); text-transform: uppercase; }
  .skills { list-style: none; font-size: 6px; line-height: 10px; color: var(--ink); }
  .bar { height: 3px; margin-bottom: 7px; background: linear-gradient(to right, var(--blue) var(--w), var(--bar-grey) var(--w)); }
</style>
</head>
<body>
<main class="cv">
  <div class="sidebar"></div>

  <h1 class="abs name">Ember Lane</h1>
  <p class="abs job-title">Your Profession / Job Title</p>

  <ul class="abs contact">
    <li>020 7946 0381 <span class="ico"></span></li>
    <li>hello@emberlane.co <span class="ico"></span></li>
    <li>www.emberlane.co <span class="ico"></span></li>
    <li>Harbour Street, Leeds <span class="ico"></span></li>
  </ul>

  <div class="abs rings">
    <div class="ring">
      <svg width="44" height="44" viewBox="0 0 44 44"><circle cx="22" cy="22" r="18" fill="none" stroke="#d6d8db" stroke-width="4"/><circle cx="22" cy="22" r="18" fill="none" stroke="#2f6aa8" stroke-width="4" stroke-dasharray="68 113" transform="rotate(-90 22 22)"/><text x="22" y="24" font-size="6" text-anchor="middle" fill="#2f6aa8" font-family="Open Sans, sans-serif">Design</text></svg>
      <p class="lbl">Layout and print work</p>
    </div>
    <div class="ring">
      <svg width="44" height="44" viewBox="0 0 44 44"><circle cx="22" cy="22" r="18" fill="none" stroke="#d6d8db" stroke-width="4"/><circle cx="22" cy="22" r="18" fill="none" stroke="#2f6aa8" stroke-width="4" stroke-dasharray="85 113" transform="rotate(-90 22 22)"/><text x="22" y="24" font-size="6" text-anchor="middle" fill="#2f6aa8" font-family="Open Sans, sans-serif">Office</text></svg>
      <p class="lbl">Daily admin tools</p>
    </div>
    <div class="ring">
      <svg width="44" height="44" viewBox="0 0 44 44"><circle cx="22" cy="22" r="18" fill="none" stroke="#d6d8db" stroke-width="4"/><circle cx="22" cy="22" r="18" fill="none" stroke="#2f6aa8" stroke-width="4" stroke-dasharray="56 113" transform="rotate(-90 22 22)"/><text x="22" y="24" font-size="6" text-anchor="middle" fill="#2f6aa8" font-family="Open Sans, sans-serif">Sales</text></svg>
      <p class="lbl">Client facing roles</p>
    </div>
    <div class="ring">
      <svg width="44" height="44" viewBox="0 0 44 44"><circle cx="22" cy="22" r="18" fill="none" stroke="#d6d8db" stroke-width="4"/><circle cx="22" cy="22" r="18" fill="none" stroke="#2f6aa8" stroke-width="4" stroke-dasharray="96 113" transform="rotate(-90 22 22)"/><text x="22" y="24" font-size="6" text-anchor="middle" fill="#2f6aa8" font-family="Open Sans, sans-serif">Team</text></svg>
      <p class="lbl">Leading small groups</p>
    </div>
  </div>

  <div class="abs photo" role="img" aria-label="Portrait photo of the applicant"></div>

  <!-- Sidebar content -->
  <div class="abs" style="left:40px; top:236px; width:120px;">
    <h3 class="side-head">Portfolio</h3>
    <p class="side-text" style="margin-top:4px;">Website and project name<br>Case study and brief name<br>Printed work and results</p>
  </div>
  <div class="abs" style="left:40px; top:284px; width:120px;">
    <h3 class="side-head">Experience</h3>
    <p class="side-text" style="margin-top:4px;">Company Name<b>2016 - Present</b></p>
  </div>
  <p class="abs side-text" style="left:40px; top:356px;">Company Name<b>2014 - 2016</b></p>
  <p class="abs side-text" style="left:40px; top:424px;">Company Name<b>2012 - 2014</b></p>

  <div class="abs rule" style="left:40px; top:476px; width:110px;"></div>
  <div class="abs" style="left:40px; top:488px; width:120px;">
    <h3 class="side-head">Education</h3>
    <p class="side-text" style="margin-top:4px;">Northgate University<b>1998 - 2002</b></p>
    <p class="side-text" style="margin-top:12px;">Northgate University<b>2002 - 2004</b></p>
  </div>

  <div class="abs rule" style="left:40px; top:580px; width:110px;"></div>
  <div class="abs" style="left:40px; top:592px;">
    <h3 class="side-head">Business Skills</h3>
    <svg width="120" height="120" viewBox="0 0 120 120" style="margin-top:8px; display:block;">
      <g stroke="#d6d8db" stroke-width=".6">
        <line x1="8" y1="10" x2="118" y2="10"/><line x1="8" y1="35" x2="118" y2="35"/>
        <line x1="8" y1="60" x2="118" y2="60"/><line x1="8" y1="85" x2="118" y2="85"/>
        <line x1="8" y1="110" x2="118" y2="110"/>
      </g>
      <g fill="#2f6aa8">
        <rect x="14" y="50" width="6" height="60"/><rect x="32" y="30" width="6" height="80"/>
        <rect x="50" y="40" width="6" height="70"/><rect x="68" y="20" width="6" height="90"/>
        <rect x="86" y="34" width="6" height="76"/><rect x="104" y="56" width="6" height="54"/>
      </g>
      <g fill="#c5c8cc">
        <rect x="21" y="62" width="6" height="48"/><rect x="39" y="44" width="6" height="66"/>
        <rect x="57" y="52" width="6" height="58"/><rect x="75" y="38" width="6" height="72"/>
        <rect x="93" y="48" width="6" height="62"/><rect x="111" y="70" width="6" height="40"/>
      </g>
    </svg>
  </div>

  <!-- Main column -->
  <p class="abs para" style="left:192px; top:168px; width:320px;">A short profile about you goes here. Describe the kind of work you enjoy, the strengths you bring to a team and the value you add. Keep it brief and clear so a hiring manager can read it at a glance and see why you suit the role on offer today.</p>
  <div class="abs rule" style="left:192px; top:226px; width:320px;"></div>

  <div class="abs entry" style="top:284px;">
    <h4>Position Held</h4>
    <p class="para">Give a short outline of the role and your main duties here. Mention the team size, the tools you used and any results you are proud of, such as targets met or savings made over the period.</p>
  </div>
  <div class="abs entry" style="top:352px;">
    <h4>Position Held</h4>
    <p class="para">Summarise what you did in this post and what you learned. Keep each point short and focused on outcomes that matter to the next employer.</p>
  </div>
  <div class="abs entry" style="top:420px;">
    <h4>Position Held</h4>
    <p class="para">Describe your tasks and wins in this job. Note any training, awards or extra duties you took on while working here.</p>
  </div>

  <div class="abs rule" style="left:192px; top:476px; width:320px;"></div>

  <div class="abs" style="left:192px; top:488px; width:170px;">
    <h3 class="col-head">References</h3>
    <div class="entry" style="position:relative; left:8px; width:160px; margin-top:8px;">
      <h4>Course Studied</h4>
      <p class="para">Short detail on the course and grade you gained.</p>
    </div>
    <div class="entry" style="position:relative; left:8px; width:160px; margin-top:8px;">
      <h4>Course Studied</h4>
      <p class="para">Short detail on the course and grade you gained.</p>
    </div>
  </div>

  <div class="abs" style="left:192px; top:592px; width:170px;">
    <h3 class="col-head">Interests</h3>
    <p class="para" style="margin-top:8px;">Reference Name<br>Job Title<br>T: 020 7946 0112<br>E: ref@emberlane.co</p>
    <p class="para" style="margin-top:8px;">Reference Name<br>Job Title<br>T: 020 7946 0245<br>E: ref@emberlane.co</p>
  </div>

  <div class="abs" style="left:380px; top:488px; width:136px;">
    <h3 class="col-head">Expertise</h3>
    <div style="display:flex; gap:10px; margin-top:8px;">
      <ul class="skills">
        <li>Skill 1</li><li>Skill 2</li><li>Skill 3</li><li>Skill 4</li><li>Skill 5</li>
        <li>Skill 6</li><li>Skill 7</li><li>Skill 8</li><li>Skill 9</li><li>Skill 10</li>
      </ul>
      <div style="flex:1; padding-top:3.5px;">
        <div class="bar" style="--w:80%"></div><div class="bar" style="--w:65%"></div>
        <div class="bar" style="--w:90%"></div><div class="bar" style="--w:55%"></div>
        <div class="bar" style="--w:75%"></div><div class="bar" style="--w:60%"></div>
        <div class="bar" style="--w:85%"></div><div class="bar" style="--w:50%"></div>
        <div class="bar" style="--w:70%"></div><div class="bar" style="--w:95%"></div>
      </div>
    </div>
  </div>
</main>
</body>
</html>
```